Real estate investor, needing a business card that communicates warmth, integrity, empathy.

I have a logo that can be manipulated to align with the message - "Serving your home selling needs." Want it to stand out from typical real estate investor cards, and make distressed home sellers feel a connection with me. Should communicate warmth, integrity, empathy, and trustworthiness.

Target Market(s)

Distressed home owners who need to sell their homes, not using realtors.

Contact Information for Business Card

Glossy front and matte back, with a small box that is labelled "notes." I like darker blues and blacks together, but doesn't have to be, as long as it communicates trustworthiness, and a strong call to action.

Other font styles liked:
• see "must haves" above, but willing to review whatever comes my way.

Requirements
Must have
• The fonts on my logo are Aviano, Lusitana, and Marcellus. We don't have to use those, but I favor them.

```html
<!DOCTYPE html>
<html lang="en">
<head>
<meta charset="utf-8">
<title>Summit Ridge Homes – Business Card</title>
<link rel="stylesheet" href="https://fonts.googleapis.com/css2?family=Marcellus&family=Roboto:wght@400;500&display=swap">
<style>
  :root {
    --page-bg: #e4e4e4;
    --ink: #111111;
    --card-white: #ffffff;
    --card-black: #000000;
    --bronze: #9c7048;
    --bronze-light: #b08459;
    --back-dark: #86582f;
    --back-light: #b3835a;
    --gold: #d9b36a;
    --text-light: #ffffff;
  }
  * { box-sizing: border-box; margin: 0; padding: 0; }
  html, body {
    width: 1200px; height: 1200px; overflow: hidden;
    background: var(--page-bg);
  }
  .canvas { position: relative; width: 1200px; height: 1200px; }

  .card {
    position: absolute; left: 262px; width: 686px; height: 392px; overflow: hidden;
  }
  .card--front { top: 165px; background: var(--card-white); }
  .card--back {
    top: 653px;
    background: linear-gradient(160deg, var(--back-dark) 0%, #9b6c42 45%, var(--back-light) 100%);
  }

  .band { position: absolute; inset: 0; width: 686px; height: 392px; }

  .brand-name {
    position: absolute; left: 0; right: 0; text-align: center;
    font-family: "Marcellus", serif; font-size: 40px; letter-spacing: 3px;
  }
  .card--front .brand-name { top: 82px; color: var(--ink); }
  .card--back .brand-name { top: 80px; color: var(--gold); }

  .tagline {
    position: absolute; left: 0; right: 0; text-align: center;
    font-family: "Roboto", sans-serif; font-size: 15.5px;
  }
  .card--front .tagline { top: 181px; color: var(--bronze); }
  .card--back .tagline { top: 194px; color: #5a3418; opacity: .8; }

  .person {
    position: absolute; left: 40px; top: 277px;
    font-family: "Marcellus", serif; color: var(--text-light); font-size: 16.5px; line-height: 20px;
  }
  .person__name { color: var(--bronze); font-size: 24px; line-height: 30px; }
  .person__role { margin-bottom: 3px; }

  .contacts {
    position: absolute; right: 40px; top: 286px; list-style: none;
    font-family: "Marcellus", serif; color: var(--text-light); font-size: 16.5px; line-height: 20px;
  }
  .contacts li { display: flex; justify-content: flex-end; align-items: center; gap: 7px; }
  .contacts svg { width: 12px; height: 12px; fill: var(--bronze); flex: none; }

  .notes-box {
    position: absolute; left: 46px; top: 233px; width: 600px; height: 130px;
    background: var(--card-white); border-radius: 8px; padding: 14px 16px;
    font-family: "Roboto", sans-serif; font-weight: 500; font-size: 15.5px; color: var(--ink);
  }
</style>
</head>
<body>
<div class="canvas">

  <section class="card card--front">
    <svg class="band" viewBox="0 0 686 392" aria-hidden="true">
      <path d="M0 233 L80 233 L110 260 L140 233 L686 233 L686 392 L0 392 Z" fill="var(--card-black)"/>
      <path d="M0 229 L80 229 L110 256 L140 229 L686 229 L686 235 L142 235 L110 263 L78 235 L0 235 Z" fill="var(--bronze)"/>
    </svg>
    <h1 class="brand-name">Summit Ridge Homes</h1>
    <p class="tagline">Serving Your home selling Needs</p>

    <div class="person">
      <p class="person__name">Daniel Reyes</p>
      <p class="person__role">President</p>
      <p>4120 Birchwood Court</p>
      <p>Fairhaven, Alaska 99512</p>
    </div>

    <ul class="contacts">
      <li>369-555-0142
        <svg viewBox="0 0 24 24"><path d="M6.6 10.8a15.1 15.1 0 0 0 6.6 6.6l2.2-2.2c.3-.3.7-.4 1-.2 1.1.4 2.3.6 3.6.6.6 0 1 .4 1 1V20c0 .6-.4 1-1 1A17 17 0 0 1 3 4c0-.6.4-1 1-1h3.5c.6 0 1 .4 1 1 0 1.3.2 2.5.6 3.6.1.3 0 .7-.2 1z"/></svg>
      </li>
      <li>369-555-0187
        <svg viewBox="0 0 24 24"><path d="M7 1h10a2 2 0 0 1 2 2v18a2 2 0 0 1-2 2H7a2 2 0 0 1-2-2V3a2 2 0 0 1 2-2zm0 3v14h10V4z"/></svg>
      </li>
      <li>hello@summitridgehomes.com
        <svg viewBox="0 0 24 24"><path d="M2 5h20v14H2zm2 2v.3l8 5 8-5V7z"/></svg>
      </li>
      <li>www.summitridgehomes.com
        <svg viewBox="0 0 24 24"><path d="M12 2a10 10 0 1 0 0 20 10 10 0 0 0 0-20zm-1 17.9A8 8 0 0 1 4.2 10L9 15v1a2 2 0 0 0 2 2zm6.9-2.5A2 2 0 0 0 16 16h-1v-3a1 1 0 0 0-1-1H8v-2h2a1 1 0 0 0 1-1V7h2a2 2 0 0 0 2-2v-.4a8 8 0 0 1 2.9 12.8z"/></svg>
      </li>
    </ul>
  </section>

  <section class="card card--back">
    <h2 class="brand-name">Summit Ridge Homes</h2>
    <p class="tagline">Serving Your home selling Needs</p>
    <div class="notes-box">Notes</div>
  </section>

</div>
</body>
</html>
```